brightwave Marine

we need a business card with our new design from pixel forum that we just purchased. it needs to have our phone numbers, email address, web address and facebook address

Target Market(s)

Wealthy boat owners

Industry/Entity Type

Marine

Contact Information for Business Card

Business logo
Phone numbers Greg - 0408315962
Mandy - 0419486027
ABN - 61273059184
Email - brightwavemarineboatcleaning@examplemail.com
Web address - www.brightwavemarine.com.au
Facebook- Brightwave Marine

Number of Pages Required

1 page

Font styles to use
Serif
Sans Serif
Script

Colors
3276b5
33a6d7
474747
333333

Requirements
Must have
• Business logo and all contact details

```html
<!DOCTYPE html>
<html lang="en">
<head>
<meta charset="utf-8">
<title>Brightwave Marine – Business Card</title>
<link href="https://fonts.googleapis.com/css2?family=Roboto+Condensed:wght@400;700&display=swap" rel="stylesheet">
<style>
  :root {
    --page-bg: #e4e5e7;
    --card-black: #0a0b0d;
    --card-grey: #4a4b4e;
    --band-blue: #2c5590;
    --brand-blue: #1a5bb0;
    --ink-dark: #0b0c0e;
    --ink-light: #f2f4f8;
    --icon-grey: #9ea1a6;
  }
  * { margin: 0; padding: 0; box-sizing: border-box; }
  html, body {
    width: 1200px; height: 1200px; overflow: hidden;
    background: var(--page-bg);
    font-family: "Roboto Condensed", sans-serif;
  }
  .card {
    position: absolute; left: 76px; top: 303px;
    width: 1048px; height: 594px; overflow: hidden;
    background:
      radial-gradient(ellipse 420px 260px at 720px 330px, var(--card-grey) 0%, rgba(74,75,78,0) 100%),
      var(--card-black);
    box-shadow: 0 6px 18px rgba(0,0,0,0.25);
  }
  .info-band {
    position: absolute; left: 408px; top: 183px;
    width: 640px; height: 326px;
    background: var(--band-blue);
  }
  .logo-disc {
    position: absolute; left: -2px; top: 64px;
    width: 490px; height: 490px; border-radius: 50%;
    background: var(--card-black);
  }
  .brand-name {
    position: absolute; left: 0; top: 388px; width: 486px;
    text-align: center;
    font-weight: 700; font-size: 44px; letter-spacing: 1px;
    color: var(--brand-blue);
  }
  .phones {
    position: absolute; left: 523px; top: 212px;
    display: grid; grid-template-columns: 112px 32px auto;
    row-gap: 4px; align-items: center;
    font-weight: 700; font-size: 37px; line-height: 42px;
    color: var(--ink-dark);
  }
  .phone-icon { width: 22px; height: 34px; }
  .links {
    position: absolute; left: 514px; top: 366px;
    display: flex; flex-direction: column; gap: 6px;
    font-size: 27px; line-height: 36px; color: var(--ink-light);
  }
  .link-row { display: flex; align-items: center; white-space: nowrap; }
  .link-email { font-size: 23px; }
  .link-icon {
    width: 28px; margin-right: 12px; text-align: center;
    color: var(--icon-grey); font-size: 30px; font-style: italic;
    display: flex; justify-content: center;
  }
  .social-dot {
    width: 14px; height: 14px; border-radius: 50%;
    background: var(--icon-grey);
  }
</style>
</head>
<body>
  <div class="card">
    <div class="info-band"></div>
    <div class="logo-disc"></div>
    <div class="brand-name">Brightwave Marine</div>

    <div class="phones">
      <span>Greg</span>
      <svg class="phone-icon" viewBox="0 0 22 34" aria-hidden="true"><path d="M9 2 L4 3 C1 10 1 24 4 31 L9 32 L11 26 L8 24 C7 20 7 14 8 10 L11 8 Z" fill="#9ea1a6"/></svg>
      <span>0408315962</span>
      <span>Mandy</span>
      <svg class="phone-icon" viewBox="0 0 22 34" aria-hidden="true"><path d="M9 2 L4 3 C1 10 1 24 4 31 L9 32 L11 26 L8 24 C7 20 7 14 8 10 L11 8 Z" fill="#9ea1a6"/></svg>
      <span>0419486027</span>
      <span>ABN</span>
      <svg class="phone-icon" viewBox="0 0 22 34" aria-hidden="true"><path d="M9 2 L4 3 C1 10 1 24 4 31 L9 32 L11 26 L8 24 C7 20 7 14 8 10 L11 8 Z" fill="#9ea1a6"/></svg>
      <span>61273059184</span>
    </div>

    <div class="links">
      <div class="link-row"><span class="link-icon">@</span><span class="link-email">brightwavemarineboatcleaning@examplemail.com</span></div>
      <div class="link-row">
        <span class="link-icon">
          <svg width="26" height="26" viewBox="0 0 26 26" aria-hidden="true" fill="none" stroke="#9ea1a6" stroke-width="1.6">
            <circle cx="13" cy="13" r="11"/><ellipse cx="13" cy="13" rx="5" ry="11"/>
            <line x1="2" y1="13" x2="24" y2="13"/><line x1="4" y1="7.5" x2="22" y2="7.5"/><line x1="4" y1="18.5" x2="22" y2="18.5"/>
          </svg>
        </span>
        <span>www.brightwavemarine.com.au</span>
      </div>
      <div class="link-row"><span class="link-icon"><span class="social-dot"></span></span><span>Brightwave Marine</span></div>
    </div>
  </div>
</body>
</html>
```